Lanterns Over The Quiet Meadow Waters Book Cover

Book cover for a new book titled "Lanterns Over The Quiet Meadow Waters" which will show how retirees can pay NO tax in their retirement. Would like you to use your creative inspiration to come up with a design.

Please make MEADOW WATERS the emphasis of the title.

can you show money being rescued, or freed, from taxes.

I'm trying convey the message that retirees can FREE themselves from the burden of taxes in retirement by reading this book and following the instructions. Think about a person swimming with a weight on his back, sinking him. Suddenly the weight is removed. The feeling and imagery of the load being light now

Doing MEADOW WATERS can alleviate many of unnecessary taxes which will weight retirees down. But, unfortunately, many advisors in my industry do not educate their clients on this stuff.

Not a fan of dark backgrounds, generally speaking. Lighter is good.

Remember folks, go to brindlecart. Type in Roth IRA books. what will jump out over the stuff that's already there? Thanks!

Target Market(s)

recent, or soon to be, retirees, people in their 50s and 60s, typically couples

Industry/Entity Type

Financial

Font styles to use
Serif

Colors

Designer to choose colors to be used in the design.

Requirements
Must have
• Be optimistic, sunny, happy. How you do that? I don't know, that's why I'm hiring you. This book is designed for the lay person, (average Joe and Jane)
• Put my picture on the lower back.
• My name at bottom of the cover
Nice to have
• Be nice to have the cover POP on Brindlecart because I'm competing with so many other books and thumbnails
• Maybe a kite with a dollar bill that is breaking from a ball and chain? Just an idea.
Should not have
• No guys in suits. Happy couples sitting on the beach or sailing. That stuff is in every piece of financial planning literature.
• NOT TECHNICAL. NO PIGGY BANKS Design please

```html
<!DOCTYPE html>
<html lang="en">
<head>
<meta charset="utf-8">
<title>Lanterns Over The Quiet Meadow Waters — Book Cover</title>
<link rel="stylesheet" href="https://fonts.googleapis.com/css2?family=Cinzel:wght@400;500;600&display=swap">
<style>
  :root {
    --stage-top: #f4f6f6;
    --stage-bottom: #ddfbfd;
    --sky-deep: #2f8fd0;
    --sky-mid: #6fb6e6;
    --sky-light: #b9dcf2;
    --field-light: #4f9a3a;
    --field-deep: #2f6d24;
    --ink: #1b2a3a;
    --rule: rgba(27, 42, 58, 0.55);
    --author: #ffffff;
    --cover-edge: #ffffff;
  }
  * { box-sizing: border-box; margin: 0; padding: 0; }
  html, body {
    width: 1200px;
    height: 775px;
    overflow: hidden;
  }
  body {
    background: linear-gradient(200deg, var(--stage-top) 0%, var(--stage-bottom) 100%);
    font-family: "Cinzel", "Times New Roman", serif;
    position: relative;
  }
  .book-cover {
    position: absolute;
    left: 367px;
    top: 38px;
    width: 466px;
    height: 700px;
    overflow: hidden;
    border: 3px solid var(--cover-edge);
    box-shadow: 0 18px 40px rgba(40, 70, 90, 0.18);
  }
  .cover-photo {
    position: absolute;
    inset: 0;
    background: linear-gradient(180deg,
      var(--sky-deep) 0%,
      var(--sky-mid) 38%,
      var(--sky-light) 74%,
      var(--field-light) 76%,
      var(--field-deep) 100%);
  }
  .title-block {
    position: absolute;
    top: 108px;
    left: 36px;
    right: 36px;
    text-align: center;
    color: var(--ink);
  }
  .title-rule {
    height: 1px;
    background: var(--rule);
    margin: 0 18px;
  }
  .title-lead {
    font-size: 24px;
    font-weight: 500;
    letter-spacing: 2px;
    line-height: 1.25;
    padding: 10px 0 6px;
  }
  .title-lead .small-word {
    font-size: 17px;
  }
  .title-main {
    font-size: 80px;
    font-weight: 600;
    line-height: 1;
    letter-spacing: 1px;
    padding-top: 6px;
  }
  .title-sub {
    font-size: 44px;
    font-weight: 500;
    letter-spacing: 3px;
    line-height: 1.1;
    padding-bottom: 12px;
  }
  .author-name {
    position: absolute;
    bottom: 44px;
    left: 0;
    right: 0;
    text-align: center;
    color: var(--author);
    font-size: 20px;
    font-weight: 400;
    letter-spacing: 3px;
  }
</style>
</head>
<body>
  <article class="book-cover">
    <div class="cover-photo" role="img" aria-label="Photograph of a bright blue sky with soft white clouds and a sunburst over a green meadow"></div>

    <header class="title-block">
      <div class="title-rule"></div>
      <p class="title-lead">Lanterns Over<br><span class="small-word">The Quiet</span></p>
      <h1 class="title-main">MEADOW</h1>
      <p class="title-sub">WATERS</p>
      <div class="title-rule"></div>
    </header>

    <p class="author-name">Marcus Pellworth</p>
  </article>
</body>
</html>
```